Christmas Ballet Poster for El Relojero

I urgently need a poster for the El Relojero ballet, it needs to look magical and very similar to the reference attached. The title should be El Relojero and the typography and look should be as similar as possible as the words The Glassblower in the reference attached. Use a dancers photo just for reference, I will not use that photo as someone will be taking the picture of the principal dancer and we will be using that. It should look magical, upscale and pretty.
Requirements
Must have
- Title: El Relojero
- Space for date, time and prices
- Space to add logo
- It must look as similar as the reference as possible, magical, elegant.
Should not have
- Any logo

```html
<!DOCTYPE html>
<html lang="es">
<head>
<meta charset="utf-8">
<title>El Relojero — Ballet de Navidad</title>
<link rel="stylesheet" href="https://fonts.googleapis.com/css2?family=Courgette&display=swap">
<style>
  :root {
    --stage-night: #03041a;
    --stage-deep: #080b2a;
    --stage-haze: #121840;
    --spot-ice: #7fa9c9;
    --spot-glow: #cfe2f0;
    --chrome-white: #ffffff;
    --chrome-ice: #dff1fb;
    --chrome-blue: #1f5fae;
    --chrome-sky: #7fc0ec;
    --chrome-teal: #3fb5c9;
    --chrome-blush: #e7c6d6;
    --title-shadow: rgba(0, 0, 0, 0.9);
    --reserve-line: rgba(199, 226, 245, 0.22);
    --sparkle: #eaf6ff;
  }

  * { margin: 0; padding: 0; box-sizing: border-box; }

  html, body {
    width: 1200px;
    height: 540px;
    overflow: hidden;
    background: var(--stage-night);
  }

  .poster {
    position: relative;
    width: 1200px;
    height: 540px;
    overflow: hidden;
    background: var(--stage-night);
  }

  .stage-photo {
    position: absolute;
    inset: 0;
    background:
      radial-gradient(ellipse 150px 250px at 240px 300px, rgba(207, 226, 240, 0.6), rgba(127, 169, 201, 0.25) 55%, transparent 100%),
      radial-gradient(ellipse 90px 130px at 520px 470px, rgba(127, 169, 201, 0.16), transparent 100%),
      radial-gradient(ellipse 90px 130px at 890px 470px, rgba(127, 169, 201, 0.16), transparent 100%),
      radial-gradient(ellipse 70px 100px at 140px 500px, rgba(127, 169, 201, 0.14), transparent 100%),
      radial-gradient(ellipse 700px 380px at 880px 110px, var(--stage-haze), transparent 100%),
      linear-gradient(180deg, var(--stage-deep) 0%, var(--stage-night) 100%);
  }

  .sparkles {
    position: absolute;
    left: 420px;
    top: 170px;
    width: 720px;
    height: 170px;
    pointer-events: none;
  }

  .title {
    position: absolute;
    left: 771px;
    top: 178px;
    transform: translateX(-50%);
    font-family: "Courgette", cursive;
    font-weight: 400;
    font-size: 118px;
    line-height: 1.1;
    white-space: nowrap;
    letter-spacing: 3px;
    background: linear-gradient(180deg,
      var(--chrome-white) 0%,
      var(--chrome-ice) 20%,
      var(--chrome-blush) 30%,
      var(--chrome-sky) 40%,
      var(--chrome-blue) 50%,
      var(--chrome-white) 56%,
      var(--chrome-teal) 68%,
      var(--chrome-blue) 82%,
      var(--chrome-ice) 100%);
    -webkit-background-clip: text;
    background-clip: text;
    color: transparent;
    -webkit-text-stroke: 2.5px rgba(240, 248, 255, 0.9);
    filter: drop-shadow(4px 5px 4px var(--title-shadow)) drop-shadow(0 0 8px rgba(143, 195, 234, 0.45));
  }

  .event-details {
    position: absolute;
    left: 560px;
    top: 350px;
    width: 420px;
    height: 64px;
    border-top: 1px solid var(--reserve-line);
    border-bottom: 1px solid var(--reserve-line);
  }

  .logo-space {
    position: absolute;
    right: 36px;
    bottom: 30px;
    width: 84px;
    height: 84px;
    border: 1px dashed var(--reserve-line);
    border-radius: 50%;
  }
</style>
</head>
<body>
  <main class="poster">
    <div class="stage-photo" role="img" aria-label="Fotografía de escenario: la bailarina principal con tutú celeste y tiara a la izquierda, brazos en alto, con el cuerpo de baile en penumbra al fondo"></div>

    <svg class="sparkles" viewBox="0 0 720 170" aria-hidden="true">
      <g fill="var(--sparkle)">
        <path d="M40 30 l3 11 l11 3 l-11 3 l-3 11 l-3 -11 l-11 -3 l11 -3z" opacity="0.85"/>
        <path d="M190 12 l2 7 l7 2 l-7 2 l-2 7 l-2 -7 l-7 -2 l7 -2z" opacity="0.7"/>
        <path d="M395 22 l3 10 l10 3 l-10 3 l-3 10 l-3 -10 l-10 -3 l10 -3z" opacity="0.8"/>
        <path d="M610 8 l2 7 l7 2 l-7 2 l-2 7 l-2 -7 l-7 -2 l7 -2z" opacity="0.7"/>
        <path d="M690 118 l3 10 l10 3 l-10 3 l-3 10 l-3 -10 l-10 -3 l10 -3z" opacity="0.8"/>
        <path d="M270 150 l2 6 l6 2 l-6 2 l-2 6 l-2 -6 l-6 -2 l6 -2z" opacity="0.6"/>
        <circle cx="120" cy="150" r="1.6" opacity="0.7"/>
        <circle cx="330" cy="6" r="1.4" opacity="0.6"/>
        <circle cx="510" cy="150" r="1.8" opacity="0.7"/>
        <circle cx="560" cy="30" r="1.3" opacity="0.6"/>
        <circle cx="10" cy="110" r="1.5" opacity="0.6"/>
      </g>
    </svg>

    <h1 class="title">El Relojero</h1>

    <div class="event-details" aria-label="Espacio reservado para fecha, hora y precios"></div>
    <div class="logo-space" aria-label="Espacio reservado para el logotipo"></div>
  </main>
</body>
</html>
```